I need a logo design and a business card design for a new strategy consultancy that I set up called Corvanel LLC. We help clients make strategically important decisions, cutting through the cloud of noise. The design should imply clarity, simplicity and wisdom.

```html
<!DOCTYPE html>
<html lang="en">
<head>
<meta charset="utf-8">
<title>Corvanel LLC — Business Card</title>
<link rel="stylesheet" href="https://fonts.googleapis.com/css2?family=Libre+Baskerville:wght@700&family=Nunito+Sans:wght@400&display=swap">
<style>
  :root {
    --navy: #2d3558;
    --paper: #f7f7f7;
    --stage: #ececee;
    --ink: #4a4a4a;
    --rule: #c9c9c9;
  }
  * { margin: 0; padding: 0; box-sizing: border-box; }
  html, body { width: 1200px; height: 1159px; overflow: hidden; }
  body {
    background: var(--stage);
    position: relative;
    font-family: "Nunito Sans", Arial, sans-serif;
  }
  .card {
    position: absolute;
    left: 170px;
    width: 860px;
    height: 492px;
    box-shadow: 0 6px 18px rgba(0,0,0,0.12);
    overflow: hidden;
  }
  .card--front { top: 70px; background: var(--paper); }
  .card--back { top: 597px; background: var(--navy); }

  .wordmark {
    font-family: "Libre Baskerville", Georgia, serif;
    font-weight: 700;
    letter-spacing: 3px;
    text-transform: uppercase;
    display: flex;
    align-items: center;
    gap: 18px;
  }
  .wordmark__mark { width: 22px; height: 22px; display: block; }

  .card--front .wordmark {
    position: absolute;
    left: 70px; top: 170px;
    font-size: 32px;
    color: var(--navy);
  }
  .card--front .wordmark__mark { background: var(--navy); }

  .divider {
    position: absolute;
    left: 470px; top: 60px;
    width: 1px; height: 300px;
    background: var(--rule);
  }

  .contact {
    position: absolute;
    left: 515px; top: 70px;
    color: var(--ink);
    font-size: 19px;
    line-height: 1.5;
  }
  .contact__name {
    font-family: "Libre Baskerville", Georgia, serif;
    font-weight: 700;
    font-size: 27px;
    color: var(--navy);
    line-height: 1.2;
  }
  .contact__title { font-size: 18px; margin-bottom: 14px; }
  .contact__address { margin-bottom: 6px; }
  .contact__line { display: flex; align-items: center; gap: 12px; }
  .contact__line svg { width: 16px; height: 16px; flex: none; }

  .band {
    position: absolute;
    left: 0; bottom: 0;
    width: 100%; height: 60px;
    background: var(--navy);
  }

  .card--back .wordmark {
    position: absolute;
    left: 0; right: 0; top: 0; bottom: 0;
    justify-content: center;
    font-size: 40px;
    color: #f2f2f2;
  }
  .card--back .wordmark__mark { width: 28px; height: 28px; background: #f2f2f2; }
  .texture {
    position: absolute; inset: 0;
    background: var(--navy);
  }
</style>
</head>
<body>
  <section class="card card--front">
    <div class="wordmark"><span class="wordmark__mark"></span>Corvanel LLC</div>
    <div class="divider"></div>
    <div class="contact">
      <div class="contact__name">Dana Merrow</div>
      <div class="contact__title">Managing Partner</div>
      <div class="contact__address">Level 9, 14 Quarry Street<br>Sydney NSW 2000</div>
      <div class="contact__line">
        <svg viewBox="0 0 16 16"><path d="M4 1.5l2.5 3-1.4 1.6a8 8 0 0 0 4.8 4.8l1.6-1.4 3 2.5-1.6 2.2C7.5 14 2 8.5 1.8 3.1z" fill="var(--navy)"/></svg>
        000 000 0000
      </div>
      <div class="contact__line">
        <svg viewBox="0 0 16 16"><path d="M4 1.5l2.5 3-1.4 1.6a8 8 0 0 0 4.8 4.8l1.6-1.4 3 2.5-1.6 2.2C7.5 14 2 8.5 1.8 3.1z" fill="var(--navy)"/></svg>
        000 000 0000
      </div>
      <div class="contact__line">
        <svg viewBox="0 0 16 16"><rect x="1.5" y="3.5" width="13" height="9" fill="none" stroke="var(--navy)" stroke-width="1.3"/><path d="M1.5 3.5L8 9l6.5-5.5" fill="none" stroke="var(--navy)" stroke-width="1.3"/></svg>
        dana@corvanelllc.com
      </div>
      <div class="contact__line">
        <svg viewBox="0 0 16 16"><circle cx="8" cy="8" r="6.5" fill="none" stroke="var(--navy)" stroke-width="1.3"/><ellipse cx="8" cy="8" rx="2.8" ry="6.5" fill="none" stroke="var(--navy)" stroke-width="1.1"/><path d="M1.5 8h13" stroke="var(--navy)" stroke-width="1.1"/></svg>
        www.corvanelllc.com
      </div>
    </div>
    <div class="band" role="img" aria-label="Navy band with fine diamond lattice pattern"></div>
  </section>

  <section class="card card--back">
    <div class="texture" role="img" aria-label="Navy background with fine dotted diamond lattice pattern"></div>
    <div class="wordmark"><span class="wordmark__mark"></span>Corvanel LLC</div>
  </section>
</body>
</html>
```